Open House 2017

We need a flyer for an insert for a newspaper for an open house that we are going to have and we are also wanting to list the front of the flyer the 3 pictures of our real estate agents and our Logo.

For the real estate agents : The one with Purple shirt would be the middle picture.

Attached also is our current Logo, Please re-design our Logo a bit to make it look better.

Target Market(s)

Residential and commercial and Land In our rural areas.

Industry/Entity Type

House

Requirements
Must have
• Front page -
• Our logo at the top our 3 pictures at the top after our logo and business address.
• Middle of page Some thing worded similar to the following:"let us place a SOLD sign in your front yard". Or
• " Sold vs. For Sale which would you like to see in your front yard?"
• Our colors for our agency are Gold and Black (the whole flyer does not need to be this color though)
• Join us for an open house in our office
• Wednesday March 1
• 3-6pm
• Back page of flyer: "If you would like to add your name to the Sold Properties list, give us a call today!
• Sold listings which we will get sent to you will also be listed on the back page.
Should not have
• do not make the flyer too "busy" with too many pictures and wording.

```html
<!DOCTYPE html>
<html lang="en">
<head>
<meta charset="utf-8">
<title>Hartwell Realty – Open House Flyer</title>
<link rel="stylesheet" href="https://fonts.googleapis.com/css2?family=Bebas+Neue&family=Lato:wght@400;700&family=Questrial&display=swap">
<style>
  :root{
    --gold:#f2b643;
    --gold-pale:#fae0ad;
    --black:#141414;
    --ink:#1c1c1c;
    --paper:#ffffff;
    --mist:#efefef;
    --photo:#7d7d7d;
  }
  *{box-sizing:border-box;margin:0;padding:0}
  html,body{width:1200px;height:1200px;overflow:hidden;background:var(--paper)}
  .canvas{position:relative;width:1200px;height:1200px}
  .flyer{position:absolute;left:214px;top:105px;width:900px;height:1156px;transform:scale(.8571);transform-origin:0 0;background:var(--paper);box-shadow:0 0 4px rgba(0,0,0,.25);overflow:hidden;font-family:'Lato',sans-serif;color:var(--ink)}
  .header{position:absolute;left:0;top:0;width:900px;height:97px;background:var(--black)}
  .brand{position:absolute;left:25px;top:26px;width:255px;height:56px;background:#1f1f1f;display:flex;align-items:center;padding-left:14px;gap:10px;color:#fff;font-family:'Lato',sans-serif;font-weight:700;font-size:24px;white-space:nowrap}
  .brand-dot{width:14px;height:14px;border-radius:50%;background:#fff;flex:none}
  .header-address{position:absolute;right:45px;top:42px;font-size:24px;color:var(--gold);letter-spacing:.2px;white-space:nowrap}
  .team-band{position:absolute;left:0;top:104px;width:900px;height:338px;background:linear-gradient(to bottom,var(--gold),var(--gold-pale))}
  .portrait{position:absolute;border-radius:50%;border:5px solid #fff;background:radial-gradient(circle at 50% 40%,#9a9a9a,var(--photo))}
  .p1{left:41px;top:141px;width:250px;height:250px}
  .p2{left:312px;top:125px;width:276px;height:276px}
  .p3{left:610px;top:141px;width:250px;height:250px}
  .agent{position:absolute;top:442px;height:244px;font-size:14.5px;line-height:17px;white-space:nowrap}
  .agent.gold{background:var(--gold)}
  .agent.white{background:var(--paper)}
  .a1{left:0;width:296px;padding:34px 0 0 46px}
  .a2{left:296px;width:302px;padding:18px 0 0 62px}
  .a3{left:598px;width:302px;padding:18px 0 0 42px}
  .agent-name{font-family:'Questrial',sans-serif;font-size:22px;line-height:26px;margin-bottom:6px}
  .a1 .agent-name{margin-left:-2px}
  .agent p+p{margin-top:17px}
  .lower{position:absolute;left:0;top:686px;width:900px;height:399px;background:linear-gradient(to bottom,var(--mist),var(--paper))}
  .about-tag{position:absolute;left:725px;top:718px;width:175px;height:37px;background:var(--black);color:#fff;font-family:'Bebas Neue',sans-serif;font-size:36px;line-height:39px;padding-left:17px}
  .about-text{position:absolute;left:451px;top:779px;width:409px;font-size:14.3px;line-height:17px;text-align:justify;text-align-last:right}
  .headline{position:absolute;left:55px;top:0;width:390px;height:1156px;font-family:'Bebas Neue',sans-serif;font-weight:400;color:var(--ink);pointer-events:none}
  .headline span{position:absolute;left:0;display:block;white-space:nowrap}
  .h-line1{top:784px;font-size:86px;line-height:86px;letter-spacing:-1px}
  .h-line2{top:857px;font-size:92px;line-height:92px;color:var(--gold)}
  .h-line3{top:940px;font-size:58px;line-height:58px;letter-spacing:-1.5px}
  .event{position:absolute;right:37px;text-align:right;font-family:'Bebas Neue',sans-serif;white-space:nowrap}
  .event-call{top:892px;color:var(--gold);font-size:33px;line-height:33px}
  .event-address{top:930px;font-size:32px;line-height:32px;color:var(--ink)}
  .event-date{top:968px;font-size:32px;line-height:32px;color:var(--ink)}
  .footer{position:absolute;left:0;top:1085px;width:900px;height:71px;background:var(--black)}
  .footer-band{position:absolute;left:0;top:0}
  .call{position:absolute;left:77px;top:14px;font-size:30px;color:var(--ink);white-space:nowrap}
  .web{position:absolute;left:547px;top:0;height:71px;display:flex;align-items:center;gap:17px;font-size:30px;color:var(--gold);white-space:nowrap}
  .web-icon{flex:none;display:block}
</style>
</head>
<body>
<div class="canvas">
  <div class="flyer">
    <header class="header">
      <div class="brand"><span class="brand-dot"></span>Hartwell Realty LLC</div>
      <div class="header-address">12 Harbor Street | Pine Lake, Mn 55990</div>
    </header>

    <section class="team-band"></section>
    <div class="portrait p1" role="img" aria-label="Portrait photo of agent Joan Keller"></div>
    <div class="portrait p2" role="img" aria-label="Portrait photo of broker Mark Hartwell"></div>
    <div class="portrait p3" role="img" aria-label="Portrait photo of agent Dale Prentis"></div>

    <div class="agent gold a1">
      <div class="agent-name">Joan Keller</div>
      <p>Real Estate Agent<br>Licensed in Minnesota &amp; Iowa</p>
      <p>Cell Phone :(641) 555-0147<br>Office Phone: (507) 555-0100<br>E-mail:&nbsp; joan@hartwellrealty.com</p>
      <p>12 Harbor Street<br>Pine Lake, Mn 55990</p>
    </div>
    <div class="agent white a2">
      <div class="agent-name">Mark Hartwell</div>
      <p>Broker<br>Licensed in Minnesota &amp; Iowa</p>
      <p>Cell Phone :(507) 555-0182<br>Office Phone: (507) 555-0100<br>E-mail:&nbsp; mark@hartwellrealty.com</p>
      <p>12 Harbor Street<br>Pine Lake, Mn 55990</p>
    </div>
    <div class="agent gold a3">
      <div class="agent-name">Dale Prentis</div>
      <p>Real Estate Agent<br>Licensed in Minnesota &amp; Iowa</p>
      <p>Cell Phone :507-555-0139<br>Office Phone: (507) 555-0100<br>E-mail:&nbsp; dale@hartwellrealty.com</p>
      <p>12 Harbor Street<br>Pine Lake, Mn 55990</p>
    </div>

    <section class="lower"></section>
    <div class="about-tag">About Us</div>
    <p class="about-text">Hartwell Realty LLC is a real estate brokerage licensed in both Minnesota and Iowa. Our statewide coverage includes Fairbank County and Marlow County, and the cities of Pine Lake, Delmont, Elmwood, Frye, Granton, Winfield, Lake Ardell, Brinley, Ashby, Mapleford, Eastby, Kestrel, and Larkin</p>

    <h1 class="headline">
      <span class="h-line1">LET US PLACE</span>
      <span class="h-line2">A SOLD SIGN</span>
      <span class="h-line3">IN YOUR FRONT YARD</span>
    </h1>

    <div class="event event-call">JOIN US FOR AN OPEN HOUSE IN OUR OFFICE</div>
    <div class="event event-address">12 HARBOR STREET &nbsp;|&nbsp; PINE LAKE, MN 55990</div>
    <div class="event event-date">WEDNESDAY,MARCH 1 &nbsp;| 3-6PM</div>

    <footer class="footer">
      <svg class="footer-band" width="900" height="71" aria-hidden="true"><polygon points="0,0 462,0 493,71 0,71" fill="#f2b643"/></svg>
      <div class="call">CALL US : (507) 555-0100</div>
      <div class="web">
        <svg class="web-icon" width="34" height="34" viewBox="0 0 34 34" fill="none" stroke="#f2b643" stroke-width="2" aria-hidden="true">
          <circle cx="17" cy="17" r="15"/><ellipse cx="17" cy="17" rx="7" ry="15"/>
          <line x1="2" y1="17" x2="32" y2="17"/><path d="M5 9h24M5 25h24"/>
        </svg>
        <span>hartwellrealty.com</span>
      </div>
    </footer>
  </div>
</div>
</body>
</html>
```